Text heavy poster for university audience

I have developed a set of standards for online teaching that need to be turned into a post format. The project has a logo which should be incorporated. Most of the designing will be in terms of text layout. The logo (two versions - higher quality files available) and the a sample of standards (as image - word version available; the example is one third of standards) are attached. Design that can be adapted to brochure format would be great. (Brochure adaption will be paid separately via another project to be opened here). More details available here: http://www.brivelquarto.net
Updates

Dear all,

The URL for the site needs to be include in the design - either as footer or under logo:
<http://www.brivelquarto.net>

Sorry for late notice

Target Market(s)

The are university staff

Industry/Entity Type

University

Font styles to use
Serif
Sans Serif

Requirements
Must have
• The text in the "required" attachment must be included; but for initial draft feel free to restrict your design to "sample" attachment
The green from the Logo (PANTONE 17-5641 Emerald) should be the foundation of the colour palette.
Nice to have
• The collaborators as named here: http://www.brivelquarto.net/collaborators/
My preferred find is helvetica neue, but similar can be used
Should not have
• Decorative fonts

```html
<!DOCTYPE html>
<html lang="en">
<head>
<meta charset="utf-8">
<title>Brivel Quarto Standards – Online Education Poster</title>
<link rel="stylesheet" href="https://fonts.googleapis.com/css2?family=Arimo:wght@400;700&family=Tinos:wght@400&family=Heebo:wght@300&display=swap">
<style>
  :root {
    --emerald: #4f9a74;
    --emerald-panel: #5b9b7b;
    --ink: #2f3a33;
    --paper: #ffffff;
  }
  * { box-sizing: border-box; margin: 0; padding: 0; }
  html, body { width: 847px; height: 1200px; overflow: hidden; background: var(--paper); }
  .poster { position: relative; width: 847px; height: 1200px; background: var(--paper); font-family: "Arimo", Helvetica, sans-serif; color: var(--paper); }

  .disclaimer { position: absolute; left: 0; top: 0; width: 847px; height: 48px; background: var(--emerald-panel); padding: 8px 12px; font-size: 7.4px; line-height: 1.3; }

  .masthead { position: absolute; left: 0; top: 48px; width: 847px; height: 156px; }
  .brand-mark { position: absolute; left: 30px; top: 18px; width: 120px; height: 110px; background: var(--emerald); }
  .brand-name { position: absolute; left: 172px; top: 22px; font-weight: 700; font-size: 30px; line-height: 1.2; letter-spacing: 1px; color: var(--emerald); text-transform: uppercase; }
  .site-url { position: absolute; left: 174px; top: 104px; font-size: 13px; color: var(--emerald); letter-spacing: 0.3px; }
  .credit { position: absolute; left: 36px; top: 136px; font-size: 12px; font-weight: 700; letter-spacing: 3.6px; color: var(--ink); text-transform: uppercase; }
  .licence { position: absolute; left: 679px; top: 28px; width: 137px; height: 102px; border: 1px solid var(--ink); border-radius: 8px; padding: 7px; color: var(--ink); }
  .licence-head { display: flex; align-items: center; gap: 5px; font-size: 15px; font-weight: 700; margin-bottom: 5px; }
  .licence-dot { width: 20px; height: 20px; border-radius: 50%; border: 2px solid var(--ink); display: inline-block; }
  .licence p { font-size: 5.6px; line-height: 1.3; }

  .panel { position: absolute; left: 6px; top: 204px; width: 835px; height: 990px; background: var(--emerald-panel); }

  .section-title { position: absolute; font-family: "Heebo", Helvetica, sans-serif; font-weight: 300; font-size: 58px; line-height: 1; }
  .section-quote { position: absolute; font-size: 11.5px; line-height: 1.36; }

  .standard { position: absolute; display: grid; grid-template-columns: auto 1fr; column-gap: 7px; }
  .standard .num { font-family: "Tinos", "Times New Roman", serif; font-size: 24px; line-height: 1; padding-top: 1px; }
  .standard h3 { font-family: "Tinos", "Times New Roman", serif; font-weight: 400; font-size: 18.5px; line-height: 1.0; }
  .criteria { grid-column: 1 / span 2; font-size: 9px; line-height: 1.55; margin-top: 5px; }
</style>
</head>
<body>
<div class="poster">

  <div class="disclaimer">DISCLAIMER: Support for this activity has been provided by the National Office for Tertiary Teaching. The views expressed in this activity do not necessarily reflect the views of the National Office for Tertiary Teaching.</div>

  <header class="masthead">
    <div class="brand-mark"></div>
    <div class="brand-name">Brivel Quarto<br>Standards</div>
    <div class="site-url">http://www.brivelquarto.net</div>
    <div class="credit">Tomas Verrell and Collaborators</div>
    <div class="licence">
      <div class="licence-head"><span class="licence-dot"></span>openshare</div>
      <p>This work is licensed under the Open Share Attribution-ShareAlike 3.0 Unported License. To view a copy of this license, visit http://openshare-licence.org/licenses/by-sa/3.0/ or send a letter to Open Share, 12 Harbour Lane, Suite 40, Lindfield, NSW 2070.</p>
    </div>
  </header>

  <main class="panel">
    <h2 class="section-title" style="left:14px; top:6px;">Students</h2>
    <p class="section-quote" style="left:18px; top:80px; width:240px;">“Students are supported in their online learning with a quality curriculum, opportunities for interaction with peers and staff, and appropriate support.”</p>

    <section class="standard" style="left:270px; top:22px; width:270px;">
      <span class="num">1</span><h3>Curriculum materials are aligned, available and engaging.</h3>
      <p class="criteria" style="padding-left:18px;">THRESHOLD: The necessary materials are constructively aligned and available online.<br>GOOD: The materials are provided using a variety of media to engage students and support diversity.</p>
    </section>
    <section class="standard" style="left:554px; top:20px; width:272px;">
      <span class="num">2</span><h3>Learning activities are aligned, available and engaging.</h3>
      <p class="criteria" style="padding-left:18px;">THRESHOLD: Constructively aligned learning activities are available online.<br>GOOD: Learning activities use a variety of appropriate technologies to engage students and support diversity.</p>
    </section>

    <section class="standard" style="left:18px; top:148px; width:250px;">
      <span class="num">3</span><h3>Assessment tasks are aligned, available and engaging.</h3>
      <p class="criteria" style="padding-left:18px;">THRESHOLD: Constructively aligned assessment tasks are available online.<br>GOOD: Assessment tasks use a variety of appropriate technologies to engage students and support diversity.</p>
    </section>
    <section class="standard" style="left:282px; top:142px; width:264px;">
      <span class="num">4</span><h3>Students are provided with timely, improvement focused formative feedback</h3>
      <p class="criteria" style="padding-left:12px;">THRESHOLD: Appropriate technologies are used to provide students with formative feedback in a timely manner.<br>GOOD: Feedback is provided in a variety of media to engage students and support diversity.</p>
    </section>
    <section class="standard" style="left:558px; top:154px; width:266px;">
      <span class="num">5</span><h3>Students are provided with opportunities to interact with peers.</h3>
      <p class="criteria" style="padding-left:80px; margin-top:-14px;">THRESHOLD: There are opportunities for social interaction.<br>GOOD: There are opportunities for learning-focused interaction.</p>
    </section>

    <section class="standard" style="left:16px; top:268px; width:252px;">
      <span class="num">6</span><h3>Students are provided with opportunities to interact with staff.</h3>
      <p class="criteria" style="padding-left:28px; text-indent:40px; margin-top:-15px;">THRESHOLD: Staff are provided with opportunities to answer student queries.<br>GOOD: Staff are provided with opportunities to be active participants in learning-focused interactions.</p>
    </section>
    <section class="standard" style="left:286px; top:268px; width:260px;">
      <span class="num">7</span><h3>Students are provided with appropriate learning support</h3>
      <p class="criteria" style="padding-left:10px;">THRESHOLD: Appropriate, up-to-date and reliable learning guides and resources are provided online.<br>GOOD: A range of appropriate, up-to-date and reliable online learning skills workshops are available.</p>
    </section>
    <section class="standard" style="left:558px; top:266px; width:266px;">
      <span class="num">8</span><h3>Students are supported in their use of educational technology</h3>
      <p class="criteria" style="padding-left:2px;">THRESHOLD: Appropriate, up-to-date and reliable technological guides and resources are provided online.<br>GOOD: Appropriate, timely and reliable asynchronous technological support is available.</p>
    </section>

    <h2 class="section-title" style="left:14px; top:410px;">Staff</h2>
    <p class="section-quote" style="left:138px; top:402px; width:152px;">“Staff are supported in their online teaching with quality professional development, resourcing and technical support.”</p>
    <section class="standard" style="left:308px; top:396px; width:518px;">
      <span class="num">9</span><h3>Staff are provided with quality professional development in online education</h3>
      <p class="criteria" style="padding-left:24px;">THRESHOLD: A range of appropriate, up-to-date and informative professional development activities are available to staff.<br>GOOD: The organisation requires staff to engage in continued professional development relevant to online education.</p>
    </section>
    <section class="standard" style="left:30px; top:494px; width:400px;">
      <span class="num">10</span><h3>Online education is recognised in workload.</h3>
      <p class="criteria" style="padding-left:40px;">THRESHOLD: Online teaching is recognised in workload.<br>GOOD: Online unit development is recognised in workload.</p>
    </section>
    <section class="standard" style="left:442px; top:490px; width:384px;">
      <span class="num">11</span><h3 style="padding-left:10px;">Staff are supported in their use of educational technology</h3>
      <p class="criteria" style="padding-left:22px;">THRESHOLD: Appropriate, up-to-date and reliable technological guides and resources are provided online.<br>GOOD: Appropriate, timely and reliable asynchronous technological support is available.</p>
    </section>

    <h2 class="section-title" style="left:14px; top:578px;">Organisation</h2>
    <p class="section-quote" style="left:96px; top:644px; width:290px;">“The organisation supports online education through the provision of quality leadership, infrastructure, and evaluation.”</p>
    <section class="standard" style="left:446px; top:622px; width:380px;">
      <span class="num">13</span><h3>The organisation employs a systematic approach to resource allocation in online education.</h3>
      <p class="criteria" style="padding-left:40px;">THRESHOLD: There is a systematic approach to resource allocation.<br>GOOD: There is systematic approach with formal criteria that are widely available.</p>
    </section>
    <section class="standard" style="left:16px; top:702px; width:440px;">
      <span class="num">12</span><h3>The organisation provides strategic leadership in online education</h3>
      <p class="criteria">THRESHOLD: The organisation has a clearly articulated strategic position on online education.<br>GOOD: An appropriate member of the executive has explicit responsibility for online education.</p>
    </section>
    <section class="standard" style="left:462px; top:742px; width:364px;">
      <span class="num">15</span><h3>The organisation has a process for evaluating and improving student satisfaction with online education.</h3>
      <p class="criteria" style="padding-left:18px;">THRESHOLD: The organisation has a systematic process for evaluating and improving student satisfaction with online education.<br>GOOD: The organisation has a systematic process for improving student learning outcomes and satisfaction with online education and communicating improvements to students.</p>
    </section>
    <section class="standard" style="left:16px; top:784px; width:440px;">
      <span class="num">14</span><h3>The organisation maintains and supports a quality learning platform for delivering online education.</h3>
      <p class="criteria" style="padding-left:44px;">THRESHOLD: The organisation maintains and supports an appropriate learning platform.<br>GOOD: The learning platform provided is fit for purpose, scalable and reliable.</p>
    </section>
    <section class="standard" style="left:16px; top:866px; width:384px;">
      <span class="num">16</span><h3>The organisation has a process for evaluating and improving training and support for staff.</h3>
      <p class="criteria" style="padding-left:44px;">THRESHOLD: The organisation has a systematic process for evaluating and improving staff training and support.<br>GOOD: The organisation has a systematic process for improving staff training and support and communicating improvements to staff.</p>
    </section>
    <section class="standard" style="left:408px; top:884px; width:418px;">
      <span class="num">17</span><h3>The organisation has a process for evaluating and improving infrastructure.</h3>
      <p class="criteria" style="padding-left:36px;">THRESHOLD: The organisation has a systematic process for evaluating and improving infrastructure.<br>GOOD: The organisation has a systematic process for improving infrastructure and communicating improvements to stakeholders.</p>
    </section>
  </main>

</div>
</body>
</html>
```